Oil and Gas Industry training School Needs a Web Design

We need a web design for a new company based in Northern British Columbia Canada called "SKILLSPAN Industry Training Inc." Is a training facility that specializes in different aspects of Pipeline Construction training. We also offer compliance courses for Oil and Gas Industry. We would like to see designs that us the colours in our logo.

Target Market(s)

Is Men and women between 18-60 that want to work in the oil and gas industry

Industry/Entity Type

School

Number of Pages Required

5+ page

Font styles to use
Sans Serif

Colors
f37022
000000
333333
ffffff
848484
7f7f7f
c8c8c8
f68d4d
fee3d4

Requirements
Must have
• a easy back end for editing content! and adding additional pages if necessary.

```html
<!DOCTYPE html>
<html lang="en">
<head>
<meta charset="utf-8">
<title>SkillSpan Industry Training Inc.</title>
<link href="https://fonts.googleapis.com/css2?family=Jost:wght@300;400;500;600&family=Mulish:ital,wght@0,400;0,600;0,700;1,400&display=swap" rel="stylesheet">
<style>
:root{
  --orange:#f37022;
  --orange-light:#f68d4d;
  --orange-pale:#fee3d4;
  --black:#000000;
  --ink:#333333;
  --grey:#848484;
  --grey-mid:#7f7f7f;
  --grey-line:#c8c8c8;
  --white:#ffffff;
  --page-bg:#f4f5f7;
  --band-bg:#fafafa;
  --footer-bg:#2b2c2e;
  --sky:#3fb6e8;
}
*{box-sizing:border-box;margin:0;padding:0}
html,body{width:1200px;height:1000px;overflow:hidden;background:var(--white)}
body{font-family:'Mulish',sans-serif;color:var(--ink);position:relative}
.page{position:absolute;left:291px;top:12px;width:619px;height:978px;background:var(--page-bg);box-shadow:8px 8px 12px rgba(0,0,0,.35);overflow:hidden}
.abs{position:absolute}

/* header */
.site-header{left:0;top:0;width:619px;height:32px;background:var(--page-bg);border-top:1px solid var(--grey-line)}
.brand{left:81px;top:6px;display:flex;align-items:center;gap:5px}
.brand-dot{width:20px;height:20px;border-radius:50%;background:var(--orange)}
.brand-name{font-family:'Jost',sans-serif;font-weight:600;font-size:14px;color:var(--ink);line-height:1}
.brand-tag{display:block;font-size:5px;color:var(--grey);font-weight:400;letter-spacing:.3px;margin-top:2px}
.nav{left:370px;top:0;display:flex;height:32px;font-size:7px;font-weight:600;color:var(--ink)}
.nav a{display:flex;align-items:center;padding:0 4px;color:inherit;text-decoration:none;height:32px}
.nav a.active{background:#e9eaec;border-bottom:2px solid var(--orange);color:var(--grey);padding:0 5px}
.nav a small{font-size:5px;margin-left:1px;color:var(--grey)}

/* hero */
.hero{left:0;top:32px;width:619px;height:301px;background:linear-gradient(100deg,#b9bcc0 0%,#8c96a3 25%,#3e6a9c 45%,#c9a78e 62%,#e0a24f 72%,#6b7686 88%,#9ba3ad 100%)}
.hero-title{left:82px;top:99px;font-family:'Jost',sans-serif;font-weight:500;font-size:18px;color:var(--white);letter-spacing:.3px;text-shadow:0 1px 2px rgba(0,0,0,.3)}
.hero-text{left:82px;top:134px;width:120px;font-size:7px;line-height:10px;color:var(--white)}

/* intro */
.intro{left:0;top:345px;width:619px;text-align:center}
.intro h2{font-weight:400;font-size:11px;color:#555}
.intro p{font-size:6px;color:#666;margin-top:3px}

/* services */
.service{width:100px;height:100px;border-radius:50%;background:var(--white);border:1px solid #e6e7ea;text-align:center;padding-top:20px}
.service h3{font-family:'Jost',sans-serif;font-weight:600;font-size:7px;color:var(--black)}
.service p{font-size:6px;line-height:9px;color:var(--ink);margin:7px 10px 0}
.btn{display:inline-block;background:var(--orange);color:var(--white);font-size:5.5px;padding:2px 6px;margin-top:6px}

/* news */
.news{left:0;top:560px;width:619px;height:134px;background:var(--band-bg)}
.section-title{font-family:'Jost',sans-serif;font-weight:500;font-size:12px;color:var(--black);letter-spacing:.3px}
.news .section-title{left:0;width:619px;text-align:center;top:5px}
.divider{height:1px;background:#e4e5e8}
.divider::before,.divider::after{content:"";position:absolute;top:-1.5px;width:4px;height:4px;border-radius:50%;background:var(--grey-line)}
.divider::before{left:-2px}.divider::after{right:-2px}
.news-lead{left:0;top:43px;width:619px;text-align:center;font-size:6px;color:var(--ink)}
.news-lead em{font-style:normal;color:var(--orange)}
.post-thumb{width:66px;height:46px;background:linear-gradient(160deg,#c7d3de,#7c92a8 60%,#dfe5ea)}
.post-date{position:absolute;left:3px;top:4px;background:var(--sky);color:var(--white);font-size:4.5px;padding:1px 4px;white-space:nowrap}
.post-body{width:72px}
.post-body h4{font-family:'Jost',sans-serif;font-size:6.5px;font-weight:600;color:var(--black)}
.post-tags{font-size:5px;color:var(--sky);font-style:italic;margin-top:3px}
.post-tags b{display:inline-block;width:4px;height:4px;background:var(--ink);margin-right:3px;font-style:normal}
.post-body p{font-size:5.5px;line-height:8px;color:var(--ink);margin-top:2px}

/* testimonials & faq */
.col-title{font-family:'Jost',sans-serif;font-weight:300;font-size:11px;color:var(--black)}
.avatar{width:38px;height:38px;border-radius:50%;background:linear-gradient(#dfe6ee,#8fa4bb);border:2px solid var(--white)}
.quote{width:150px;font-size:5.5px;line-height:8px;font-style:italic;color:var(--grey)}
.quote-name{font-size:5.5px;color:var(--ink);margin-top:5px;font-style:normal}
.faq-row{width:223px;height:16px;background:var(--white);display:flex;align-items:center;font-size:6.5px;font-weight:700;color:var(--black)}
.faq-row span{width:21px;text-align:center;font-size:10px;font-weight:700}

/* footer */
.site-footer{left:0;top:957px;width:619px;height:21px;background:var(--footer-bg);color:#bbb;font-size:5px}
.foot-links{left:59px;top:4px;display:flex;gap:6px}
.foot-copy{left:395px;top:4px}
</style>
</head>
<body>
<div class="page">

  <header class="site-header abs">
    <div class="brand abs">
      <span class="brand-dot"></span>
      <span class="brand-name">SKILLSPAN<span class="brand-tag">INDUSTRY TRAINING INC.</span></span>
    </div>
    <nav class="nav abs">
      <a class="active" href="#">Home<small>▾</small></a>
      <a href="#">Page 2<small>▾</small></a>
      <a href="#">Page 3<small>▾</small></a>
      <a href="#">Page 4<small>▾</small></a>
      <a href="#">Contact</a>
    </nav>
  </header>

  <section class="hero abs" role="img" aria-label="Photo of a smiling pipeline worker in an orange hard hat with a colleague working at an electrical panel behind"></section>
  <h1 class="hero-title abs">SKILLSPAN - INDUSTRY TRAINING INC.</h1>
  <p class="hero-text abs">Lorem ipsum dolor sit amet, consecte adipiscing elit. Fusce at justo eget lorem port titor tincidunt.</p>

  <div class="intro abs">
    <h2>Lorem ipsum dolor sit amet, consecte adipiscing elit. Fusce at justo eget lorem port titor tincidunt.</h2>
    <p>Lorem ipsum dolor sit amet, consecte adipiscing elit. Fusce at justo eget lorem port titor tincidunt.</p>
  </div>

  <div class="service abs" style="left:74px;top:394px"><h3>Service 1</h3><p>Lorem ipsum dolor sit amet, co ctetuer adipiscing elit, sed di nonummy nibh euismod te.</p><span class="btn">Read more ›</span></div>
  <div class="service abs" style="left:195px;top:394px"><h3>Service 2</h3><p>Lorem ipsum dolor sit amet, co ctetuer adipiscing elit, sed di nonummy nibh euismod t.</p><span class="btn">Read more ›</span></div>
  <div class="service abs" style="left:316px;top:394px"><h3>Service 3</h3><p>Lorem ipsum dolor sit amet, co ctetuer adipiscing elit, sed di nonummy nibh euismod t.</p><span class="btn">Read more ›</span></div>
  <div class="service abs" style="left:437px;top:394px"><h3>Service 4</h3><p>Lorem ipsum dolor sit amet, co ctetuer adipiscing elit, sed di nonummy nibh euismod t.</p><span class="btn">Read more ›</span></div>

  <section class="news abs">
    <h2 class="section-title abs">OUR LATEST NEWS</h2>
    <div class="divider abs" style="left:233px;top:31px;width:155px"></div>
    <p class="news-lead abs">Lorem ipsum dolor sit amen, coctetuer adipiscing elit, sed di <em>nonummy</em> nibh euismod te.</p>

    <div class="post-thumb abs" style="left:84px;top:69px" role="img" aria-label="Photo of students at computer workstations"><span class="post-date">December 12, 2012</span></div>
    <div class="post-body abs" style="left:156px;top:70px"><h4>This is the Post's title</h4><div class="post-tags"><b></b>tag, post, card, rock</div><p>Lorem ipsum dolor sit am tuer adipiscing elit, sed ummy nibh euismod.</p></div>

    <div class="post-thumb abs" style="left:242px;top:69px" role="img" aria-label="Photo of students at computer workstations"><span class="post-date">April 24, 2012</span></div>
    <div class="post-body abs" style="left:313px;top:70px"><h4>Just some Title</h4><div class="post-tags"><b></b>tag, post, card, rock</div><p>Lorem ipsum dolor sit am tuer adipiscing elit, sed ummy nibh euismod.</p></div>

    <div class="post-thumb abs" style="left:400px;top:69px" role="img" aria-label="Photo of students at computer workstations"><span class="post-date">December 12, 2012</span></div>
    <div class="post-body abs" style="left:472px;top:70px"><h4>This is the Post's title</h4><div class="post-tags"><b></b>tag, post, card, rock</div><p>Lorem ipsum dolor sit am tuer adipiscing elit, sed ummy nibh euismod.</p></div>
  </section>

  <h2 class="col-title abs" style="left:81px;top:756px">TESTIMONIALS</h2>
  <div class="divider abs" style="left:83px;top:782px;width:200px"></div>
  <div class="avatar abs" style="left:77px;top:799px" role="img" aria-label="Portrait photo of a client"></div>
  <p class="quote abs" style="left:125px;top:800px">"Lorem ipsum dolor sit amet, cons tuer adipiscing elit, sed diam nonummy nibh euismod. cons tuer adipiscing elit, sed.- Lorem ipsum dolor sit amet."<span class="quote-name" style="display:block">Sam Carter, CEO</span></p>
  <div class="abs" style="left:125px;top:852px;width:155px;height:1px;background:#e4e5e8"></div>
  <div class="abs" style="left:124px;top:850px;width:4px;height:4px;border-radius:50%;background:var(--sky)"></div>
  <div class="avatar abs" style="left:77px;top:866px" role="img" aria-label="Portrait photo of a client"></div>
  <p class="quote abs" style="left:125px;top:867px">"Lorem ipsum dolor sit amet, cons tuer adipiscing elit, sed diam nonummy nibh euismod. cons tuer adipiscing elit, sed.- Lorem ipsum dolor sit amet."<span class="quote-name" style="display:block">Sam Carter, CEO</span></p>

  <h2 class="col-title abs" style="left:316px;top:756px">FREQUENTLY ASKED QUESTIONS</h2>
  <div class="divider abs" style="left:318px;top:782px;width:200px"></div>
  <div class="faq-row abs" style="left:316px;top:798px"><span>+</span>How to question goes here?</div>
  <div class="faq-row abs" style="left:316px;top:816px"><span>+</span>How to question goes here?</div>
  <div class="faq-row abs" style="left:316px;top:834px"><span>+</span>How to question goes here?</div>
  <div class="faq-row abs" style="left:316px;top:852px"><span>+</span>How to question goes here?</div>
  <div class="faq-row abs" style="left:316px;top:870px"><span>+</span>How to question goes here?</div>

  <footer class="site-footer abs">
    <div class="foot-links abs"><span>HOME</span><span>PAGE 2</span><span>PAGE 3</span><span>PAGE 4</span><span>CONTACT</span></div>
    <div class="foot-copy abs">SkillSpan © 2014 Industry Training Inc. | All Rights Reserved</div>
  </footer>
</div>
</body>
</html>
```